A new fitness program IRON FORGE 8X needs to create a new mini-mag

We need the following word doc turned into a similar look and feel to our other programs (also attached). Images will be provided. It doesn't need to be over complex, but needs to keep the high quality and standards of our other booklets that focuses on male fitness and health.
The design includes creating the cover as well using a similar format to the example provided.

```html
<!DOCTYPE html>
<html lang="en">
<head>
<meta charset="utf-8">
<title>Iron Forge 8X – 28 Day Primer Program</title>
<link rel="stylesheet" href="https://fonts.googleapis.com/css2?family=Archivo+Black&family=Cinzel:wght@400;600&family=Lobster&family=Playfair+Display:ital,wght@1,900&family=Open+Sans:wght@400;600&display=swap">
<style>
  :root {
    --sky-top: #8fb8dc;
    --sky-mid: #a9cbe8;
    --sky-low: #c3dbef;
    --title-red: #8c2b27;
    --ink: #2f3338;
    --white: #ffffff;
    --accent-yellow: #eee08a;
    --photo-warm: #c9a288;
    --photo-cool: #a7c3dc;
  }
  * { margin: 0; padding: 0; box-sizing: border-box; }
  html, body { width: 927px; height: 1200px; overflow: hidden; }
  body { background: var(--sky-mid); }

  .cover {
    position: relative;
    width: 927px;
    height: 1200px;
    overflow: hidden;
    background: linear-gradient(180deg, var(--sky-top) 0%, var(--sky-mid) 45%, var(--sky-low) 100%);
  }

  .hero-photo {
    position: absolute;
    left: 0;
    top: 195px;
    width: 420px;
    height: 1005px;
    background: linear-gradient(180deg, var(--photo-cool) 0%, var(--photo-warm) 35%, var(--photo-warm) 75%, var(--photo-cool) 100%);
    opacity: 0.85;
  }

  .cover-title {
    position: absolute;
    top: 54px;
    left: 0;
    width: 927px;
    text-align: center;
    font-family: "Archivo Black", sans-serif;
    font-size: 52px;
    color: var(--title-red);
    letter-spacing: 0.5px;
    text-shadow: 2px 3px 3px rgba(0,0,0,0.35);
    white-space: nowrap;
  }

  .principles-intro {
    position: absolute;
    top: 134px;
    left: 0;
    width: 927px;
    text-align: center;
    font-family: "Cinzel", serif;
    font-size: 39px;
    color: var(--ink);
    white-space: nowrap;
  }
  .principles-intro .small { font-size: 30px; }

  .principle-list {
    position: absolute;
    left: 532px;
    top: 198px;
    list-style: none;
  }
  .principle {
    display: flex;
    align-items: center;
    height: 72px;
    font-family: "Cinzel", serif;
    font-size: 42px;
    color: var(--ink);
  }
  .principle svg { width: 44px; height: 44px; margin-right: 36px; }

  .focus-line {
    position: absolute;
    font-family: "Lobster", cursive;
    color: var(--white);
    font-size: 38px;
    line-height: 1;
    white-space: nowrap;
    text-shadow: 1px 1px 2px rgba(0,0,0,0.25);
  }
  .focus-word {
    font-size: 45px;
    color: var(--accent-yellow);
    letter-spacing: 1px;
  }
  .focus-mindset { right: 28px; top: 470px; }
  .focus-training { right: 28px; top: 536px; }
  .focus-understand { left: 479px; top: 604px; }
  .focus-nutrition { left: 479px; top: 642px; }

  .motto {
    position: absolute;
    left: 455px;
    top: 800px;
    width: 465px;
    text-align: center;
    font-family: "Playfair Display", serif;
    font-style: italic;
    font-weight: 900;
    color: var(--white);
    font-size: 40px;
    line-height: 1.2;
    white-space: nowrap;
    text-shadow: 2px 3px 4px rgba(0,0,0,0.45);
  }
  .motto .big { font-size: 50px; }

  .brand-block {
    position: absolute;
    right: 24px;
    top: 1056px;
    text-align: right;
    font-family: "Open Sans", sans-serif;
    color: var(--white);
    white-space: nowrap;
  }
  .brand-name { font-size: 25px; }
  .brand-tagline { font-size: 28px; margin-top: 2px; letter-spacing: -0.5px; }
  .brand-tagline .sep { color: var(--accent-yellow); }
  .brand-web {
    display: flex;
    align-items: center;
    justify-content: flex-end;
    gap: 22px;
    margin-top: 2px;
    font-size: 26px;
  }
  .brand-mark {
    width: 52px; height: 52px;
    border-radius: 50%;
    border: 3px solid var(--white);
  }
</style>
</head>
<body>
<main class="cover">
  <div class="hero-photo" role="img" aria-label="Photo of a fit man in sunglasses and board shorts standing by the sea"></div>

  <h1 class="cover-title">28 DAY “PRIMER” PROGRAM</h1>
  <p class="principles-intro">E<span class="small">NHANCE YOUR LIFE WITH THE</span> 3 CORE P<span class="small">RINCIPLES</span></p>

  <ul class="principle-list">
    <li class="principle">
      <svg viewBox="0 0 44 44" aria-hidden="true"><rect x="3" y="10" width="28" height="28" fill="none" stroke="#2f3338" stroke-width="3"/><path d="M9 22 L17 31 L40 4" fill="none" stroke="#2f3338" stroke-width="5" stroke-linecap="round" stroke-linejoin="round"/></svg>
      MOTIVATION
    </li>
    <li class="principle">
      <svg viewBox="0 0 44 44" aria-hidden="true"><rect x="3" y="10" width="28" height="28" fill="none" stroke="#2f3338" stroke-width="3"/><path d="M9 22 L17 31 L40 4" fill="none" stroke="#2f3338" stroke-width="5" stroke-linecap="round" stroke-linejoin="round"/></svg>
      EDUCATION
    </li>
    <li class="principle">
      <svg viewBox="0 0 44 44" aria-hidden="true"><rect x="3" y="10" width="28" height="28" fill="none" stroke="#2f3338" stroke-width="3"/><path d="M9 22 L17 31 L40 4" fill="none" stroke="#2f3338" stroke-width="5" stroke-linecap="round" stroke-linejoin="round"/></svg>
      HABIT
    </li>
  </ul>

  <p class="focus-line focus-mindset">Create a dominant <span class="focus-word">MINDSET</span></p>
  <p class="focus-line focus-training">Maximize your <span class="focus-word">TRAINING</span></p>
  <p class="focus-line focus-understand">Understand the world of</p>
  <p class="focus-line focus-nutrition"><span class="focus-word">NUTRITION</span></p>

  <p class="motto">Life’s too short to be<br><span class="big">‘AVERAGE’</span>. It’s<br>time to be the<br><span class="big">‘BEST’</span>!</p>

  <footer class="brand-block">
    <p class="brand-name">IRON FORGE 8X</p>
    <p class="brand-tagline">MOTIVATION<span class="sep">|</span>EDUCATION<span class="sep">|</span>DOMINATION</p>
    <p class="brand-web"><span class="brand-mark" aria-hidden="true"></span>www.ironforge8x.com</p>
  </footer>
</main>
</body>
</html>
```